Brindle Mox brochure

We need a brochure design for a new company based in Australia called BrindleMox. We are a internet marketing company that adds business to Australian internet directories, Maps, GPS devices and search engines. The system is currently being used in the U.S. and we are bringing it to Australia.
The design should communicate that business owners are going to get more customers coming to their business, more profit and be easily found on the internet and Mobile phones.
At this stage we do not have a logo and are open to the colours that are used.

Target Market(s)

Business owners with Bricks and mortar business. Individuals or large chains or franchises

Industry/Entity Type

Internet

Requirements
Must have
• We have a 100% Guarentee
If your business is not on Page 1 or 2 of Plimbo within 4 months we continue for Free.

Price is $99 per month.
Nice to have
• Bullet points
*Make sure you are seen on maps, directories, Plimbo, and GPS devices.
*Consumers use local search to shop and find businesses today.
*Consumers use Mobile devices to search for your product and service.

```html
<!DOCTYPE html>
<html lang="en">
<head>
<meta charset="utf-8">
<title>Brindlemox Brochure</title>
<link rel="stylesheet" href="https://fonts.googleapis.com/css2?family=Questrial&display=swap">
<style>
  :root{
    --page:#e8e9ec;
    --navy:#0b0f4c;
    --navy-deep:#07093d;
    --royal:#2b5aae;
    --cyan:#22b8ee;
    --sky:#3ab4f0;
    --brand-blue:#2a9fe2;
    --ink:#4a4a4a;
    --heading:#2a5fae;
    --promo:#3d8fd9;
    --white:#ffffff;
  }
  *{box-sizing:border-box;margin:0;padding:0}
  html,body{width:1200px;height:900px;overflow:hidden}
  body{background:var(--page);font-family:"Questrial",sans-serif;position:relative}
  .brochure{position:absolute;left:30px;top:15px;width:1140px;height:870px;display:flex;box-shadow:0 4px 14px rgba(0,0,0,.25)}
  .panel{position:relative;width:380px;height:870px;overflow:hidden}
  .panel > svg.shapes{position:absolute;inset:0;width:380px;height:870px}
  .panel-about{background:var(--white)}
  .about-title{position:absolute;left:32px;top:318px;font-size:29px;color:var(--heading);font-weight:400;display:flex;align-items:center;gap:12px}
  .about-title .dot{width:7px;height:7px;border-radius:50%;background:var(--sky);display:inline-block}
  .about-body{position:absolute;left:27px;top:360px;width:328px;font-size:13.6px;line-height:19.4px;color:var(--ink);text-align:justify}
  .about-body p{margin-bottom:19px}
  .about-points{list-style:none;margin-bottom:19px}
  .about-points li{position:relative;padding-left:14px;text-align:left}
  .about-points li::before{content:"";position:absolute;left:0;top:7px;width:6px;height:6px;border-radius:50%;background:var(--sky)}
  .contact-bar{position:absolute;left:0;bottom:0;width:380px;height:60px;display:flex;align-items:center;gap:14px;padding-left:18px;font-size:28px}
  .contact-bar.email{background:var(--navy);color:var(--sky)}
  .contact-bar.web{background:var(--cyan);color:var(--navy)}
  .panel-cover{background:var(--royal)}
  .brand{position:absolute;font-weight:400;line-height:1}
  .cover-brand{left:0;width:380px;top:678px;text-align:center}
  .cover-brand .name{font-size:33px;color:var(--white)}
  .cover-brand .tag{font-size:11px;letter-spacing:1.5px;color:var(--white);margin-top:5px}
  .address{position:absolute;left:0;width:380px;top:748px;text-align:center;color:var(--white);font-size:17px;line-height:25px}
  .panel-guarantee{background:var(--navy-deep)}
  .back-brand{left:55px;width:300px;top:76px;text-align:right}
  .back-brand .name{font-size:46px;color:var(--brand-blue)}
  .back-brand .tag{font-size:15px;letter-spacing:1.5px;color:var(--white);margin-top:6px}
  .promo{position:absolute;left:48px;top:755px;color:var(--promo)}
  .promo .headline{font-size:27px}
  .promo .sub{font-size:11px;margin-top:2px}
  .promo .sub span{font-size:19px}
  .bullet-row{position:absolute;left:44px;top:832px;display:flex;gap:35px}
  .bullet-row i{width:23px;height:23px;border-radius:50%;display:block}
</style>
</head>
<body>
<main class="brochure">

  <section class="panel panel-about">
    <svg class="shapes" viewBox="0 0 380 870">
      <defs>
        <linearGradient id="globeTone" x1="0" y1="0" x2="0" y2="1">
          <stop offset="0" stop-color="#dcebf8"/>
          <stop offset=".55" stop-color="#3f88cf"/>
          <stop offset="1" stop-color="#12336f"/>
        </linearGradient>
      </defs>
      <path role="img" aria-label="Globe above a crowd of business people in silhouette" d="M0 0H380V195Q230 300 0 292Z" fill="url(#globeTone)"/>
      <path d="M0 292Q230 300 380 195" fill="none" stroke="var(--navy)" stroke-width="7"/>
    </svg>
    <h2 class="about-title">About Us <span class="dot"></span><span class="dot"></span><span class="dot"></span><span class="dot"></span><span class="dot"></span><span class="dot" style="background:var(--royal)"></span></h2>
    <div class="about-body">
      <p>Brindlemox brings a proven U.S. internet marketing system to Australia, built for business owners with bricks and mortar stores.</p>
      <p>We add your business to Australian internet directories, maps, GPS devices and search engines, so more customers find you and walk through your door. Whether you run a single shop, a large chain or a franchise, you will be easily found on the internet and on mobile phones, bringing more business and more profit.</p>
      <ul class="about-points">
        <li>Be seen on maps, directories, Plimbo and GPS devices.</li>
        <li>Consumers use local search to shop and find businesses today.</li>
        <li>Consumers use mobile devices to search for your product and service.</li>
        <li>If you are not on Page 1 or 2 of Plimbo within 4 months, we continue for free.</li>
      </ul>
    </div>
    <div class="contact-bar email">
      <svg width="40" height="30" viewBox="0 0 40 30" aria-hidden="true">
        <rect x="2" y="4" width="36" height="24" rx="2" fill="var(--sky)"/>
        <path d="M2 6L20 18L38 6" fill="none" stroke="var(--navy)" stroke-width="2.5"/>
      </svg>
      <span>info@brindlemox.com</span>
    </div>
  </section>

  <section class="panel panel-cover">
    <svg class="shapes" viewBox="0 0 380 870">
      <defs>
        <radialGradient id="burstTone" cx=".48" cy=".42" r=".75">
          <stop offset="0" stop-color="#cfe6ff"/>
          <stop offset=".15" stop-color="#3f78d8"/>
          <stop offset=".55" stop-color="#10245e"/>
          <stop offset="1" stop-color="#03061c"/>
        </radialGradient>
      </defs>
      <path role="img" aria-label="Light burst over a digital globe tiled with portraits of people" d="M0 0H380V560Q140 575 0 680Z" fill="url(#burstTone)"/>
      <path d="M0 680Q140 575 380 558" fill="none" stroke="var(--white)" stroke-width="4"/>
    </svg>
    <div class="brand cover-brand">
      <div class="name">Brindlemox</div>
      <div class="tag">internet marketing</div>
    </div>
    <div class="address">00 Floor Complex Street<br>City Name 000 111</div>
    <div class="contact-bar web">
      <svg width="40" height="40" viewBox="0 0 40 40" aria-hidden="true" fill="none" stroke="var(--navy)" stroke-width="2">
        <circle cx="20" cy="20" r="17"/>
        <ellipse cx="20" cy="20" rx="8" ry="17"/>
        <path d="M3 20H37M6 11H34M6 29H34M20 3V37"/>
      </svg>
      <span>www.brindlemox.com</span>
    </div>
  </section>

  <section class="panel panel-guarantee">
    <svg class="shapes" viewBox="0 0 380 870">
      <defs>
        <linearGradient id="handTone" x1="0" y1="0" x2="1" y2="1">
          <stop offset="0" stop-color="#eceef1"/>
          <stop offset=".6" stop-color="#d9dde2"/>
          <stop offset="1" stop-color="#c4c9cf"/>
        </linearGradient>
        <linearGradient id="edgeGlow" x1="0" y1="0" x2="1" y2="0">
          <stop offset="0" stop-color="#2a6fd0" stop-opacity=".2"/>
          <stop offset=".6" stop-color="#3aa8ee"/>
          <stop offset="1" stop-color="#2a6fd0" stop-opacity=".3"/>
        </linearGradient>
      </defs>
      <path role="img" aria-label="Hand drawing a network diagram with a 100% guarantee stamp" d="M0 262Q220 255 380 155V690Q220 725 0 722Z" fill="url(#handTone)"/>
      <path d="M0 250Q220 245 380 150" fill="none" stroke="url(#edgeGlow)" stroke-width="5"/>
      <path d="M0 735Q220 738 380 680" fill="none" stroke="url(#edgeGlow)" stroke-width="5"/>
    </svg>
    <div class="brand back-brand">
      <div class="name">Brindlemox</div>
      <div class="tag">internet marketing</div>
    </div>
    <div class="promo">
      <div class="headline">100% GUARANTEE</div>
      <div class="sub">or we continue for free. Only <span>$99 per month</span></div>
    </div>
    <div class="bullet-row" aria-hidden="true">
      <i style="background:#1fb8f0"></i><i style="background:#1caae8"></i><i style="background:#1d93da"></i><i style="background:#1e79c8"></i><i style="background:#1f60b6"></i><i style="background:#2449a2"></i>
    </div>
  </section>

</main>
</body>
</html>
```